Fahrzeugbeschriftung für Zahnarztpraxis
Zielgruppe
Zahnarztpraxis. Das jetzige Logo ist bereits von grafikmarkt
Aufgabenstellung
Bestandslogo und dieses Grün verwenden . ( ist von Euch ) . Damals wurde ein Wettbewerb von der Zahnarztpraxis ausgeschrieben . Adresse und Kontaktdaten sollten hervorgehoben werde.
Lustig mit Wiedererkennungseffekt ( Zahnfee muss nicht sein ) die zukünftigen Folien sollten auf die Flächen und die veloran stimmig passen

```html
<!DOCTYPE html>
<html lang="de">
<head>
<meta charset="utf-8">
<title>Fahrzeugbeschriftung LUMEN Zahnärzte</title>
<link rel="stylesheet" href="https://fonts.googleapis.com/css2?family=Ubuntu+Condensed&family=Ubuntu:wght@500;700&display=swap">
<style>
  :root {
    --backdrop: #eeeeee;
    --panel: #ffffff;
    --panel-edge: #d6d6d6;
    --brand-green: #336a1f;
    --lime: #c6dc3c;
    --slate: #6b7079;
    --ink: #3c3f44;
    --band-dark: #1f2410;
    --band-black: #111111;
    --art-blue: #d9ebf8;
    --art-green: #9ccf5a;
  }
  * { box-sizing: border-box; margin: 0; padding: 0; }
  html, body { width: 1200px; height: 900px; overflow: hidden; }
  body {
    background: var(--backdrop);
    font-family: "Ubuntu Condensed", "Arial Narrow", sans-serif;
    color: var(--ink);
    position: relative;
  }

  /* Door panel */
  .door-panel {
    position: absolute; left: 100px; top: 250px; width: 270px; height: 470px;
    background: var(--panel); border: 1px solid var(--panel-edge); border-radius: 6px;
    overflow: hidden;
  }
  .fairy-artwork {
    position: absolute; left: 25px; top: 40px; width: 220px; height: 320px;
    border-radius: 18px;
    background: linear-gradient(160deg, var(--art-blue) 0%, #e8f2d6 55%, var(--art-green) 100%);
  }
  .phone-band {
    position: absolute; left: 0; right: 0; bottom: 0; height: 78px;
    background: var(--band-black);
    display: flex; align-items: center; justify-content: center; gap: 10px;
    color: var(--lime); font-size: 26px; letter-spacing: 0.5px;
    white-space: nowrap;
  }
  .phone-band svg { width: 26px; height: 26px; flex: none; }

  /* Cargo box side */
  .box-panel {
    position: absolute; left: 400px; top: 180px; width: 700px; height: 580px;
    background: var(--panel); border: 1px solid var(--panel-edge); border-radius: 8px;
    overflow: hidden;
  }
  .web-line {
    position: absolute; left: 46px; top: 28px;
    display: flex; align-items: center; gap: 8px;
    font-size: 36px; color: var(--ink); white-space: nowrap;
  }
  .web-line svg { width: 30px; height: 30px; }
  .practice-name {
    position: absolute; left: 46px; top: 112px;
    font-family: "Ubuntu", sans-serif; font-weight: 500;
    color: var(--brand-green); line-height: 1; white-space: nowrap;
  }
  .practice-name .name-main { display: block; font-size: 118px; letter-spacing: 4px; }
  .practice-name .name-sub { display: block; font-size: 62px; letter-spacing: 3px; margin-top: 12px; }
  .dentists {
    position: absolute; left: 46px; top: 368px;
    display: flex; white-space: nowrap;
  }
  .dentist { padding: 0 20px; font-size: 26px; letter-spacing: 1px; }
  .dentist:first-child { padding-left: 0; border-right: 2px solid var(--slate); }
  .dentist .title { display: block; color: var(--slate); margin-left: 24px; }
  .dentist:last-child .title { margin-left: 0; }
  .dentist .person { display: block; color: var(--ink); margin-top: 22px; }
  .dentist .person b { font-family: "Ubuntu", sans-serif; font-weight: 700; font-size: 23px; }
  .mail-line {
    position: absolute; left: 50px; top: 490px;
    display: flex; align-items: center; gap: 8px; font-size: 28px; color: var(--ink);
    white-space: nowrap;
  }
  .mail-line svg { width: 26px; height: 26px; }
  .address-band {
    position: absolute; left: 0; right: 0; bottom: 0; height: 48px;
    background: var(--band-dark);
    display: flex; align-items: center; justify-content: center; gap: 8px;
    color: var(--lime); font-size: 28px; white-space: nowrap;
  }
  .address-band svg { width: 24px; height: 24px; }
</style>
</head>
<body>

<section class="door-panel">
  <div class="fairy-artwork" role="img" aria-label="Illustration einer Zahnfee im grünen Kleid mit Krone, die einen Zahn hält, mit geschwungenem Slogan-Schriftzug"></div>
  <div class="phone-band">
    <svg viewBox="0 0 24 24" fill="none" stroke="currentColor" stroke-width="1.6" stroke-linecap="round" stroke-linejoin="round"><path d="M5 3h4l2 5-2.5 1.5a11 11 0 0 0 6 6L16 13l5 2v4a2 2 0 0 1-2 2A16 16 0 0 1 3 5a2 2 0 0 1 2-2"/></svg>
    <span>(04321) 56 78 90</span>
  </div>
</section>

<section class="box-panel">
  <div class="web-line">
    <svg viewBox="0 0 24 24" fill="none" stroke="var(--brand-green)" stroke-width="1.6"><circle cx="12" cy="12" r="10"/><ellipse cx="12" cy="12" rx="4.5" ry="10"/><path d="M2 12h20M4 7h16M4 17h16"/></svg>
    <span>www.zahn-lumen.de</span>
  </div>

  <h1 class="practice-name">
    <span class="name-main">LUMEN</span>
    <span class="name-sub">ZAHNÄRZTE</span>
  </h1>

  <div class="dentists">
    <div class="dentist">
      <span class="title">DR. MED. DENT.</span>
      <span class="person">KONRAD <b>HALBER</b></span>
    </div>
    <div class="dentist">
      <span class="title">DR. MED. DENT.</span>
      <span class="person">MATTHIAS <b>KERNER</b></span>
    </div>
  </div>

  <div class="mail-line">
    <svg viewBox="0 0 24 24" fill="none" stroke="var(--brand-green)" stroke-width="1.6" stroke-linejoin="round"><path d="M2 10 22 3l-7 19-3-8z"/><path d="M12 14 22 3"/></svg>
    <span>praxis@zahn-lumen.de</span>
  </div>

  <div class="address-band">
    <svg viewBox="0 0 24 24" fill="none" stroke="currentColor" stroke-width="1.6"><path d="M12 22s7-7 7-12a7 7 0 0 0-14 0c0 5 7 12 7 12z"/><circle cx="12" cy="10" r="2.5"/></svg>
    <span>Lindenallee 14 • 54290 Talberg</span>
  </div>
</section>

</body>
</html>
```